Lena Hartwell Web

Lena Hartwell is a singer/songwriter that has a presence in the market for over 20 years. She currently has a website, lenahartwell.example that needs a major makeover. IT needs to be reorganized to; 1) make it more user friendly; 2) enable multi-languages including; Spanish, French, Russian, Japanese, Chinese and Portuguese; 3) enable purchases online through a storefront of promotional merchandise and music tracks. She has a logo that needs an update, as well as we currently have a business card open on PixelBazaar for input. Working to re-brand, or refresh her brand.

Lena Hartwell is the next Rosa Delmont! She has 5 platinum records, Lumen Award nominations and tours with Harold Prescott globally and is Nora Vandermeer's key backup singer for 12 years.
Updates

Some common questions have come up.  Here is some further input:

1) Colors - No specific color in mind but probably earth tones.  Although at this point we''re completely open.  Mary likes classical style, Russian, French decor.  Paris architecture. Greek, Italian textures, Goddess like symbols from the Roman Empire, or the symbols and pomp of the British monarchy.  One name on tap for the new CD is "Lanterns Over Quiet Water"
2) Example website - I have not found a new one specifically, but what I don''t like about the existing one is it is not easy to navigate.  Needs to be streamlined and easy to navigate with a storefront for merchandise and music downloads.  
3) On Logo - We''re revamping a "Global" merchandise rollout logo.  We''ve also considered possibly modifying the old english "Hartwell" family crest which signifies royalty, but have not explored that too much.  The hexagon yellow logo on her current website, I was thinking of modifying to gold (brushed - or polished?), then taking the LH lettering using a fountain pen type look there the line thickness flows with pressure on the pen, then make the gold look like a pillow, with the letter making an impression into the gold pillow.  This expands to a high quality pin, blinged up broach with diamonds imbedded for example, Global label identity, tee shirts, label tag on fashion clothing etc etc. 
 4) One thing marketing has asked us to build is a routine video blog to reach out to fans in a personal way.  Short clips of daily activity, travel prep for shows, etc. Possibly a signup/fanpage where people get emails sent back whenever anything new is posted, like a video blog, new pics, new events.  A menu to choose what you get updates on. 

Thanks, Dennis

Target Market(s)

1) Fan base in Europe, Asia, Latin America and North America
2) Movie producers seeking soundtracks
3) Private clients seeking an outstanding performer for corporate events

Industry/Entity Type

Singer

Requirements
Must have
• Better organization into smaller pages. Items critical include: 1) music tracks, 2) ClipStream links, 3) photos & Video, 4) storefront to enable online merchandise purchase 5) a way to illustrate her genre from; gospel, to rock, funk, R&B, country,

```html
<!DOCTYPE html>
<html lang="en">
<head>
<meta charset="utf-8">
<title>Lena Hartwell</title>
<link href="https://fonts.googleapis.com/css2?family=Lora:ital,wght@0,400;0,700;1,400;1,700&family=Caveat:wght@700&display=swap" rel="stylesheet">
<style>
:root{
  --bg:#16141c;
  --panel:#1d1b24;
  --gold:#f2c200;
  --gold-dark:#c99a00;
  --cyan:#5fd3e8;
  --text:#e6e2ea;
  --muted:#b9b3c2;
  --purple:#3a2048;
  --teal:#163844;
}
*{margin:0;padding:0;box-sizing:border-box}
html,body{width:816px;height:1200px;overflow:hidden;background:var(--bg)}
body{font-family:'Lora',Georgia,serif;color:var(--text);position:relative}
.abs{position:absolute}

/* header */
.site-header{left:0;top:0;width:816px;height:70px;background:linear-gradient(90deg,#1c2a33,#2a1f35 50%,#1e1b26)}
.brand{left:50px;top:12px;display:flex;align-items:center;gap:10px}
.brand-mark{width:40px;height:40px;border-radius:50%;background:var(--gold)}
.brand-name{font-size:26px;color:var(--gold);font-weight:700}
.audio-tab{left:310px;top:0;width:80px;height:40px;background:#3a1f40;transform:skewX(-12deg);display:flex;align-items:center;justify-content:center}
.audio-tab span{transform:skewX(12deg);font-size:9px;font-weight:700;color:#fff}
.social-strip{left:415px;top:0;width:345px;height:40px;background:linear-gradient(90deg,#3c3448,#4a4256);transform:skewX(-12deg)}
.social-links{left:440px;top:12px;display:flex;gap:8px;font-size:9px;color:#9fd6f0;font-weight:700}
.contact-mail{left:600px;top:12px;display:flex;align-items:center;gap:6px;font-size:11px;font-weight:700;color:#fff}
.contact-mail svg{display:block}

/* navigation */
.main-nav{left:0;top:70px;width:816px;height:44px;background:linear-gradient(#2b2930,#141318);border-bottom:1px solid #3a3642}
.nav-home{left:50px;top:70px;width:100px;height:44px;background:linear-gradient(var(--gold),var(--gold-dark));clip-path:polygon(14% 0,100% 0,86% 100%,0 100%)}
.nav-list{left:50px;top:70px;height:44px;display:flex;list-style:none;font-size:14px;color:#cfc9d4}
.nav-list li{height:44px;line-height:44px;text-align:center}
.nav-list li.active{color:#3a1a00}

/* hero */
.hero{left:0;top:114px;width:816px;height:374px;background:
  linear-gradient(0deg,rgba(8,6,12,.9) 0%,rgba(10,8,14,.55) 20%,rgba(10,8,14,0) 42%),
  radial-gradient(circle 42px at 42% 80%,rgba(130,150,255,.65),rgba(130,150,255,0) 100%),
  radial-gradient(circle 48px at 70% 77%,rgba(120,140,255,.55),rgba(120,140,255,0) 100%),
  radial-gradient(ellipse 70px 170px at 39% 44%,rgba(190,120,180,.55),rgba(190,120,180,0) 100%),
  radial-gradient(ellipse 150px 210px at 7% 32%,rgba(150,140,150,.38),rgba(150,140,150,0) 100%),
  radial-gradient(ellipse 170px 200px at 74% 26%,rgba(130,105,95,.32),rgba(130,105,95,0) 100%),
  radial-gradient(ellipse 260px 220px at 40% 35%,rgba(110,60,110,.55),rgba(110,60,110,0) 100%),
  linear-gradient(90deg,#3a3439,#2c2230 40%,#2b2029 70%,#1e1a22)}
.hero-headline{right:56px;top:246px;text-align:right;font-family:'Caveat',cursive;font-size:44px;line-height:52px;color:#fff}

/* middle */
.middle{left:0;top:488px;width:816px;height:395px;background:linear-gradient(110deg,var(--teal) 0%,#1d2230 35%,var(--purple) 70%,#241c2c)}
.card-stack{width:300px;height:136px}
.card-stack .layer{position:absolute;inset:0;border-radius:3px}
.card-stack .l1{background:#6a8a7a;transform:rotate(1.2deg) translate(4px,6px)}
.card-stack .l2{background:#b09b3c;transform:rotate(-1deg) translate(-3px,-3px)}
.card-stack .face{background:linear-gradient(90deg,#0e0d12 45%,#2a2830);border-radius:3px;overflow:hidden}
.card-photo{position:absolute;right:0;top:0;width:110px;height:100%;background:linear-gradient(90deg,#141318,#5a4e48)}
.card-title{position:absolute;left:13px;top:12px;font-size:15px;font-weight:700;font-style:italic;color:var(--cyan);white-space:nowrap}
.featured-date{position:absolute;left:13px;top:52px;font-size:13px;font-style:italic;color:#b5b1ba}
.featured-lead{position:absolute;left:13px;top:74px;font-size:14px;line-height:18px;font-weight:700;font-style:italic;color:#fff}
.event-list{position:absolute;left:11px;top:39px;list-style:none;font-size:10.5px;line-height:14.3px;color:#e8e4ea}
.event-list li:first-child{color:var(--gold)}
.event-list li::before{content:"♪";margin-right:3px}

.welcome{left:400px;top:500px;width:357px}
.welcome h1{font-size:17px;font-weight:400;font-style:italic;color:#fff;display:flex;align-items:baseline;gap:6px}
.welcome h1 em{font-size:24px;color:var(--gold);font-style:italic}
.welcome h1 .rule{flex:1;height:1px;background:var(--gold);align-self:flex-end;margin-bottom:6px}
.welcome p{font-size:8.6px;line-height:10.8px;color:#dcd8e0;margin-top:8px}
.section-rule{height:1px;background:var(--gold);position:relative}
.rule-tag{position:absolute;right:0;width:22px;height:22px;background:var(--gold);clip-path:polygon(100% 0,100% 100%,0 100%)}

.video-panel{left:400px;top:710px;width:358px;height:143px;background:#25232b;border-radius:4px;border:1px solid #34313b}
.video-head{position:absolute;left:0;top:0;width:100%;height:34px;background:#0f0e12;border-radius:4px 4px 0 0;display:flex;align-items:center;gap:8px;padding-left:9px}
.video-head h2{font-size:14px;font-weight:700;font-style:italic;color:var(--gold)}
.video-screen{position:absolute;left:8px;top:38px;width:138px;height:90px;background:linear-gradient(#2a5aa8,#3f7ad0 60%,#1c2e58);border:1px solid #444}
.video-controls{position:absolute;left:8px;top:120px;width:138px;height:9px;background:#111;font-size:5px;color:#999;padding-left:22px;line-height:9px}
.video-quote{position:absolute;left:156px;top:42px;font-size:7.4px;font-style:italic;color:var(--gold)}
.playlist{position:absolute;left:154px;top:56px;width:192px;list-style:none;background:#0d0c10;border-right:4px solid #0d0c10}
.playlist li{font-size:6.4px;font-weight:700;font-style:italic;color:#fff;height:13px;line-height:13px;padding-left:6px;border-bottom:1px solid #3a3840}
.playlist li.current{background:var(--gold);color:#2a1a00}
.share-dot{position:absolute;right:10px;bottom:8px;width:8px;height:8px;background:#3aa64a;border-radius:1px}

/* gallery */
.gallery{left:0;top:883px;width:816px;height:159px;background:linear-gradient(90deg,#131d24,#17151c 50%,#1b1620)}
.gallery-title{left:65px;top:897px;width:692px;display:flex;align-items:flex-end;gap:4px}
.gallery-title h2{font-size:18px;font-weight:400;font-style:italic;color:var(--gold);white-space:nowrap}
.gallery-title .rule-wrap{flex:1;position:relative;height:22px}
.gallery-title .section-rule{position:absolute;left:0;right:0;bottom:0}
.gallery-title .rule-tag{bottom:0}
.gallery-grid{left:65px;top:932px;display:flex;gap:21px}
.gallery-grid .photo{width:157px;height:92px}

/* footer */
.site-footer{left:0;top:1042px;width:816px;height:158px;background:linear-gradient(100deg,#1a1522,#2a1a30 45%,#16131a)}
.footer-heading{font-size:13px;font-weight:400;color:var(--gold)}
.footer-links{left:64px;top:1058px}
.footer-links ul{list-style:none;display:grid;grid-template-columns:68px 80px;row-gap:13px;margin-top:11px;font-size:9.2px;color:#bdb8c4}
.footer-links li::before{content:"";display:inline-block;width:4px;height:4px;border:1px solid #8a8490;margin-right:3px;vertical-align:1px}
.footer-links li.active{color:#fff}
.footer-links li.active::before{border-color:var(--gold)}
.contact-form{left:292px;top:1058px;width:164px}
.field{border:1px solid #6a3a6a;background:#1a1420;height:16px;margin-top:6px;font-size:8px;font-style:italic;color:#9a94a2;padding:2px 6px}
.field.area{height:35px}
.submit{margin-top:7px;display:inline-block;background:var(--gold);color:#2a1a00;font-size:10.5px;font-weight:700;padding:2px 9px;border-radius:2px}
.newsletter{left:551px;top:1060px;width:206px;display:flex;align-items:center;gap:8px}
.newsletter .input{flex:1;border-bottom:1px solid var(--gold);font-size:9px;font-style:italic;color:var(--gold);padding-bottom:1px;position:relative}
.newsletter .go{width:15px;height:14px;background:var(--gold);display:flex;align-items:center;justify-content:center}
.store-badge{left:551px;top:1092px;width:206px;height:70px;background:var(--gold);border-radius:3px;border:2px solid #e0a800}
.store-badge .title{position:absolute;left:70px;top:9px;font-size:16.5px;line-height:17px;font-weight:700;color:#1a1410}
.store-badge .sub{position:absolute;left:18px;top:53px;font-size:9.5px;font-style:italic;font-weight:700;color:#1a1410}
.store-badge svg{position:absolute}
.copyright{left:551px;top:1170px;font-size:7.8px;color:#cfcad4}
</style>
</head>
<body>

<header class="site-header abs"></header>
<div class="brand abs"><span class="brand-mark"></span><span class="brand-name">Lena Hartwell</span></div>
<div class="audio-tab abs"><span>TRACKHAVEN</span></div>
<div class="social-strip abs"></div>
<div class="social-links abs"><span>Friendly</span><span>Chirper</span><span>LinkWork</span><span>Feed</span></div>
<div class="contact-mail abs">
  <svg width="16" height="14" viewBox="0 0 16 14"><rect width="16" height="14" rx="2" fill="#2a8be0"/><path d="M3 4l5 4 5-4" stroke="#fff" stroke-width="1.4" fill="none"/></svg>
  info@lenahartwell.example
</div>

<nav class="main-nav abs"></nav>
<div class="nav-home abs"></div>
<ul class="nav-list abs">
  <li class="active" style="width:104px">Home</li>
  <li style="width:78px">Events</li>
  <li style="width:78px">Music</li>
  <li style="width:70px">Video</li>
  <li style="width:92px">Pictures</li>
  <li style="width:78px">About</li>
  <li style="width:112px">Discography</li>
  <li style="width:82px">Contact</li>
</ul>

<section class="hero abs" role="img" aria-label="Stage photo of the singer performing with a microphone under spotlights above a crowd of raised hands, with faded portraits at both sides"></section>
<div class="hero-headline abs">Lorem ipsum dolor sit amet<br>Isque est consequat</div>

<section class="middle abs"></section>

<article class="card-stack abs" style="left:65px;top:520px">
  <div class="layer l1"></div><div class="layer l2"></div>
  <div class="layer face">
    <div class="card-photo" role="img" aria-label="Portrait of the singer in profile wearing a drop earring"></div>
    <h2 class="card-title">Featured Musician Stories</h2>
    <p class="featured-date">February 04, 2013</p>
    <p class="featured-lead">Lorem ipsum dolor sit<br>amet consectetur.</p>
  </div>
</article>

<article class="card-stack abs" style="left:65px;top:712px">
  <div class="layer l1"></div><div class="layer l2"></div>
  <div class="layer face">
    <div class="card-photo" role="img" aria-label="Black and white photo of the singer on stage"></div>
    <h2 class="card-title">Available for These Events</h2>
    <ul class="event-list">
      <li>Riverside Folklife Festival</li>
      <li>Court Legends Red Carpet Gala</li>
      <li>Granite Park Summer Pride</li>
      <li>Lena Hartwell on TrackHaven</li>
      <li>Lena Hartwell Band</li>
      <li>Merry Christmas – Lena Hartwell</li>
    </ul>
  </div>
</article>

<section class="welcome abs">
  <h1>Welcome to <em>Lena Hartwell</em><span class="rule"></span></h1>
  <p>Lorem ipsum dolor sit amet, consectetur adipiscing elit. Sed pellentesque rhoncus sapien in gravida. Sed cursus nibh eu sollicitudin pellentesque. Fusce feugiat nec dolor in venenatis.</p>
  <p>Donec laoreet enim eu laoreet consectetur. Vestibulum rhoncus aliquet quam et posuere. Quisque id ante vitae neque ornare convallis. In sagittis placerat est, sit amet faucibus justo mattis id. Donec laoreet enim eu laoreet consectetur. Vestibulum rhoncus aliquet quam et posuere. Quisque id ante vitae neque ornare convallis.</p>
  <p>In sagittis placerat est, sit amet faucibus justo mattis id. Ut sed nibh ornare, viverra quam sed, pellentesque ligula.</p>
  <div class="section-rule" style="margin-top:22px"><span class="rule-tag" style="bottom:0"></span></div>
</section>

<section class="video-panel abs">
  <div class="video-head">
    <svg width="20" height="20" viewBox="0 0 20 20"><circle cx="10" cy="10" r="8.5" stroke="#f2c200" stroke-width="2" fill="none"/><path d="M8 6l6 4-6 4z" fill="#f2c200"/></svg>
    <h2>Lena Hartwell Latest Video</h2>
  </div>
  <div class="video-screen" role="img" aria-label="Video still of the singer performing on a blue-lit stage"></div>
  <div class="video-controls">0:27 / 1:38</div>
  <p class="video-quote">"Lorem ipsum dolor sit amet consect adipiscing...</p>
  <ol class="playlist">
    <li class="current">1. Lena Hartwell recording Evening Harbor</li>
    <li>2. Lena Hartwell - Live Sessions</li>
    <li>3. KVRN Bayside Radio - Lena Hartwell</li>
    <li>4. Groovetown &amp; Lena Hartwell live</li>
    <li>5. Lena Hartwell - Quiet Hours</li>
  </ol>
  <span class="share-dot"></span>
</section>

<section class="gallery abs"></section>
<div class="gallery-title abs">
  <h2>Lena Hartwell Photo Gallery</h2>
  <div class="rule-wrap"><div class="section-rule"><span class="rule-tag"></span></div></div>
</div>
<div class="gallery-grid abs">
  <div class="photo" role="img" aria-label="Singer in a red satin gown leaning on a bar" style="background:linear-gradient(90deg,#6a6258,#b23a3a 50%,#5a5850)"></div>
  <div class="photo" role="img" aria-label="Singer in red seated in a warmly lit room" style="background:linear-gradient(90deg,#c86a20,#d8472a 50%,#e0a050)"></div>
  <div class="photo" role="img" aria-label="Close portrait of the singer in a fur coat" style="background:linear-gradient(90deg,#3a2a20,#a47a5a 50%,#c89a60)"></div>
  <div class="photo" role="img" aria-label="Studio portrait of the singer against a brown backdrop" style="background:linear-gradient(90deg,#b07850,#5a3a28 60%,#2a1a14)"></div>
</div>

<footer class="site-footer abs"></footer>
<nav class="footer-links abs">
  <h3 class="footer-heading">Link</h3>
  <ul>
    <li class="active">Home</li><li>Pictures</li>
    <li>Events</li><li>About</li>
    <li>Music</li><li>Discvography</li>
    <li>Video</li><li>Contact</li>
  </ul>
</nav>
<form class="contact-form abs">
  <h3 class="footer-heading">Conatct Us</h3>
  <div class="field">Name</div>
  <div class="field">Email</div>
  <div class="field area">Message</div>
  <span class="submit">Submit</span>
</form>
<div class="newsletter abs">
  <svg width="15" height="11" viewBox="0 0 15 11"><rect width="15" height="11" fill="#8a8690"/><path d="M0 0l7.5 6L15 0" stroke="#2a2630" fill="none"/></svg>
  <span class="input">your email...</span>
  <span class="go"><svg width="8" height="8" viewBox="0 0 8 8"><path d="M1 0l7 4-7 4 2-4z" fill="#1a1410"/></svg></span>
</div>
<div class="store-badge abs">
  <svg style="left:14px;top:8px" width="50" height="40" viewBox="0 0 50 40"><path d="M2 14L8 2h34l6 12z" fill="#d23a2a"/><rect x="6" y="14" width="38" height="24" fill="#f4efe4" stroke="#6a3a2a"/><rect x="11" y="20" width="10" height="18" fill="#5a8ac8"/><rect x="26" y="20" width="13" height="10" fill="#5a8ac8"/></svg>
  <span class="title">Find Store<br>Location</span>
  <svg style="left:166px;top:6px" width="30" height="44" viewBox="0 0 30 44"><path d="M15 43C5 27 1 21 1 14a14 14 0 0 1 28 0c0 7-4 13-14 29z" fill="#d8202a" stroke="#7a0a10"/><circle cx="15" cy="14" r="8" fill="#fff"/><path d="M15 9v10M10 14h10" stroke="#d8202a" stroke-width="3"/></svg>
  <span class="sub">online merchandise purchase</span>
</div>
<p class="copyright abs">Copyright © 2013 Lena Hartwell. All rights reserved.</p>

</body>
</html>
```